Epoxy Flooring Contractor business card

We need a business card to promote a new addition to our business. We now offer Epoxy Flooring. We would like for the business card to include the images attached. One is our logo, the other is a sample of metallic epoxy flooring, we would like to incorporate that somewhere into the design. I was thinking an icon of a man pushing a concrete grinder and have the color set to the metallic epoxy color. I found a business card sample on this website, I will attach it. It has the icon that we are looking for, or something similar.
Our company name is Brightmore Coatings LLC
Our owners name is Dana Pellow
Phone is 561-847-2916
website is www.brightmore-coatingsllc.com
please let me know if you need any other info

Contact Information for Business Card

Brightmore Coatings LLC
Dana Pellow, owner
Phone: 561-847-2916
Address: P.O Box 8146 Lake Worth, FL 33471
www.Brightmore-CoatingsLLC.com
BrightmoreCoatingsLLC@mailvista.net
Include logo attached
It must include a Clip art of man with concrete grinder
Must include metallic epoxy design attached
Must include the following text
Residential Garage Flooring
Epoxy Countertops
Commercial Epoxy Flooring
Restaurant Flooring
Warehouse Flooring
Licensed & Insured
Free Estimates

Colors

Designer to choose colors to be used in the design.

Requirements
Must have
• Include logo attached
• It must include a Clip art of man with concrete grinder
• Must include metallic epoxy design attached
• Must include the following text
• Garage Epoxy Flooring
• Residential Epoxy Flooring
• Concrete Floor Crack Repairs
• Concrete Floor Grinding
• Commercial & Warehouse Epoxy Flooring
• Restaurant Epoxy Flooring
• Epoxy Countertops
• Non Slip Epoxy Pool Decks
• Textured Finishes, Flakes, Granite Coat, Metallic & Quartz
• FREE ESTIMATES • LICENSED & INSURED

```html
<!DOCTYPE html>
<html lang="en">
<head>
<meta charset="utf-8">
<title>Brightmore Coatings – Business Card</title>
<link href="https://fonts.googleapis.com/css2?family=Mulish:wght@400;600;800&family=Exo+2:wght@600&display=swap" rel="stylesheet">
<style>
  :root {
    --stage: #2b2e33;
    --white: #ffffff;
    --band-blue: #3e5f87;
    --ink-grey: #6a6a6a;
    --figure-blue: #4d6e97;
    --epoxy-deep: #1f4c94;
    --epoxy-mid: #3a6cb8;
    --epoxy-light: #7fa3d8;
    --pale: #e8eef8;
    --accent-square: #4f7ab8;
  }
  * { box-sizing: border-box; margin: 0; padding: 0; }
  html, body { width: 1200px; height: 900px; overflow: hidden; background: var(--stage); }
  body { position: relative; font-family: "Mulish", sans-serif; }

  .card {
    position: absolute; left: 300px; width: 600px; height: 340px;
    overflow: hidden; border-radius: 3px;
  }
  /* ---------- back: services ---------- */
  .card--services { top: 70px; }
  .epoxy-surface {
    position: absolute; inset: 0;
    background:
      radial-gradient(ellipse 60% 50% at 25% 30%, var(--epoxy-light) 0%, transparent 70%),
      radial-gradient(ellipse 50% 60% at 80% 70%, var(--epoxy-mid) 0%, transparent 75%),
      radial-gradient(ellipse 40% 40% at 60% 15%, #9db9e2 0%, transparent 70%),
      var(--epoxy-deep);
  }
  .services-figure {
    position: absolute; left: 40px; top: 18px; width: 70px; height: 78px;
    background: var(--pale); opacity: .85; border-radius: 4px;
  }
  .services-rule {
    position: absolute; left: 110px; top: 96px; width: 460px; height: 1px;
    background: rgba(255,255,255,.6);
  }
  .services-brand {
    position: absolute; right: 34px; top: 34px;
    display: flex; align-items: center; gap: 12px;
  }
  .brand-square { width: 38px; height: 38px; background: var(--white); }
  .brand-name {
    font-family: "Mulish", sans-serif; font-weight: 800; font-size: 22px;
    line-height: 1.05; letter-spacing: 2px; color: var(--white);
  }
  .services-list {
    position: absolute; right: 30px; top: 112px; list-style: none; text-align: right;
    font-family: "Exo 2", sans-serif; font-weight: 600; font-size: 12.5px;
    line-height: 19.5px; color: var(--white); text-transform: uppercase; letter-spacing: .4px;
  }
  .services-list li::after {
    content: ""; display: inline-block; width: 5px; height: 5px; margin-left: 8px;
    background: var(--pale); vertical-align: middle;
  }

  /* ---------- front: contact ---------- */
  .card--contact { top: 480px; background: var(--white); }
  .contact-band {
    position: absolute; left: 0; right: 0; top: 168px; bottom: 0; background: var(--band-blue);
  }
  .contact-brand {
    position: absolute; left: 40px; top: 46px; display: flex; align-items: center; gap: 14px;
  }
  .contact-brand .brand-square { background: var(--accent-square); width: 44px; height: 44px; }
  .contact-brand .brand-name { color: var(--ink-grey); font-size: 26px; }
  .contact-rule {
    position: absolute; left: 40px; top: 132px; width: 330px; height: 1px; background: var(--band-blue);
  }
  .grinder-figure {
    position: absolute; left: 385px; top: 62px; width: 175px; height: 150px;
    background: var(--figure-blue); border-radius: 4px;
  }
  .contact-details {
    position: absolute; left: 40px; top: 190px; list-style: none;
    color: var(--white); font-size: 14px; line-height: 25px;
  }
  .contact-details li { display: flex; align-items: center; gap: 8px; }
  .contact-details svg { width: 12px; height: 12px; flex: none; }
  .contact-details .no-icon { padding-left: 20px; }
  .owner {
    position: absolute; right: 34px; bottom: 26px; text-align: right; color: var(--white);
  }
  .owner-name { font-weight: 800; font-size: 24px; letter-spacing: .5px; }
  .owner-role { font-size: 15px; }
</style>
</head>
<body>

<section class="card card--services">
  <div class="epoxy-surface" role="img" aria-label="Blue metallic epoxy floor texture"></div>
  <div class="services-figure" role="img" aria-label="Silhouette of a man pushing a concrete grinder"></div>
  <div class="services-rule"></div>
  <div class="services-brand">
    <span class="brand-square"></span>
    <span class="brand-name">Brightmore<br>Coatings</span>
  </div>
  <ul class="services-list">
    <li>Garage Epoxy Flooring</li>
    <li>Residential Epoxy Flooring</li>
    <li>Concrete Floor Crack Repairs</li>
    <li>Concrete Floor Grinding</li>
    <li>Commercial &amp; Warehouse Epoxy Flooring</li>
    <li>Restaurant Epoxy Flooring</li>
    <li>Epoxy Countertops</li>
    <li>Non Slip Epoxy Pool Decks</li>
    <li>Textured Finishes, Flakes, Granite Coat, Metallic &amp; Quartz</li>
    <li>Free Estimates • Licensed &amp; Insured</li>
  </ul>
</section>

<section class="card card--contact">
  <div class="contact-band"></div>
  <div class="contact-brand">
    <span class="brand-square"></span>
    <span class="brand-name">Brightmore<br>Coatings</span>
  </div>
  <div class="contact-rule"></div>
  <div class="grinder-figure" role="img" aria-label="Silhouette of a man pushing a concrete grinder"></div>
  <ul class="contact-details">
    <li class="no-icon">P.O Box 8146 Lake Worth, FL 33471</li>
    <li>
      <svg viewBox="0 0 24 24" aria-hidden="true"><path fill="#fff" d="M6.6 10.8a15 15 0 0 0 6.6 6.6l2.2-2.2a1 1 0 0 1 1-.25 11.4 11.4 0 0 0 3.6.6 1 1 0 0 1 1 1V20a1 1 0 0 1-1 1A17 17 0 0 1 3 4a1 1 0 0 1 1-1h3.5a1 1 0 0 1 1 1c0 1.25.2 2.45.6 3.6a1 1 0 0 1-.25 1z"/></svg>
      561-847-2916
    </li>
    <li>
      <svg viewBox="0 0 24 24" aria-hidden="true"><rect x="2" y="5" width="20" height="14" fill="#fff"/><path d="M2 5l10 8 10-8" fill="none" stroke="#3e5f87" stroke-width="2"/></svg>
      BrightmoreCoatingsLLC@mailvista.net
    </li>
    <li>
      <svg viewBox="0 0 24 24" aria-hidden="true"><g fill="none" stroke="#fff" stroke-width="2"><circle cx="12" cy="12" r="10"/><ellipse cx="12" cy="12" rx="4" ry="10"/><path d="M2 12h20"/></g></svg>
      www.Brightmore-CoatingsLLC.com
    </li>
  </ul>
  <div class="owner">
    <div class="owner-name">Dana Pellow</div>
    <div class="owner-role">owner</div>
  </div>
</section>

</body>
</html>
```